fernvale junk clearing

A 6 flyer design.......
I have up loaded our company logo ....must use
A location map...........must use
and our business card with our contact information......please add all contact info
our ph. number must bold and prominent feature.....use use

A reliable Asbestos Removal & Demolition service that you can trust. All our services are offered at realistic prices and delivered on time. We operate 24 / 7 and provide free no-obligation quotes with good old fashion service.

We service the following towns and surrounding areas 7
days a week & 24 hours
Kempsey
Taree
South West Rocks
foster / Tuncurry
Coffs harbour
Nambucca Heads
Newcastle
Maitland
Singleton
Muswellbrook
Upper Hunter Valley
Central Coast
Tamworth
Armidale
this is an easy design as I have most of the theme and colours

```html
<!DOCTYPE html>
<html lang="en">
<head>
<meta charset="utf-8">
<title>Fernvale Junk Clearing – Flyer</title>
<link rel="stylesheet" href="https://fonts.googleapis.com/css2?family=Russo+One&family=Oswald:wght@500;700&family=Mulish:ital,wght@0,600;0,700;1,500;1,600&display=swap">
<style>
  :root {
    --green: #2fbf26;
    --green-dark: #1c8f17;
    --yellow: #ffe600;
    --ink: #2b2e33;
    --slate: #5a6670;
    --panel: #cfe0da;
    --grey-text: #4a4f57;
    --white: #ffffff;
  }
  * { box-sizing: border-box; margin: 0; padding: 0; }
  html, body { width: 859px; height: 1200px; overflow: hidden; background: var(--white); }
  .flyer { position: relative; width: 859px; height: 1200px; background: var(--white); }
  .frame {
    position: absolute; left: 51px; top: 50px; width: 758px; height: 1111px;
    border: 5px solid var(--green); outline: 2px solid var(--yellow); outline-offset: -8px;
  }
  .brand-name {
    position: absolute; left: 0; width: 859px; top: 78px; text-align: center;
    font-family: "Russo One", sans-serif; font-weight: 400; font-size: 36px; line-height: 42px;
    color: var(--green-dark); letter-spacing: 1px; text-transform: uppercase;
  }
  .brand-name span { display: block; }
  .service-tiles { position: absolute; top: 167px; left: 248px; display: flex; gap: 11px; }
  .service-tiles .tile { width: 117px; height: 116px; border-radius: 14px; background: var(--yellow); }
  .tagline {
    position: absolute; left: 0; width: 859px; top: 287px; text-align: center;
    font-family: "Mulish", sans-serif; font-style: italic; font-weight: 600;
    color: var(--green); font-size: 20px; line-height: 24px;
  }
  .tagline small { display: block; font-size: 15px; line-height: 18px; font-weight: 500; }
  .services-headline {
    position: absolute; left: 63px; width: 733px; top: 341px; text-align: center;
    font-family: "Russo One", sans-serif; font-weight: 400; font-size: 23.5px; line-height: 30px;
    color: var(--green); white-space: nowrap;
    -webkit-text-stroke: 1px var(--green-dark);
  }
  .contact-web {
    position: absolute; left: 0; width: 859px; top: 402px; text-align: center;
    font-family: "Mulish", sans-serif; font-weight: 700; color: var(--grey-text);
    font-size: 15px; line-height: 25px;
  }
  .contact-web strong { font-size: 19px; font-weight: 600; }
  .service-panel {
    position: absolute; left: 138px; top: 474px; width: 594px; height: 667px;
    background: var(--panel); border: 8px solid var(--slate);
  }
  .panel-intro {
    position: absolute; left: 29px; top: 20px;
    font-family: "Oswald", sans-serif; font-weight: 700; font-size: 23px; line-height: 30px; color: var(--ink);
  }
  .supervisor {
    position: absolute; left: 0; width: 578px; top: 98px; text-align: center; white-space: nowrap;
    font-family: "Oswald", sans-serif; font-weight: 500; font-size: 33px; line-height: 40px; color: var(--white);
    -webkit-text-stroke: 1.4px var(--ink); paint-order: stroke fill;
  }
  .phone-feature {
    position: absolute; left: 0; width: 578px; top: 148px; text-align: center;
    font-family: "Oswald", sans-serif; font-weight: 700; font-size: 56px; line-height: 70px;
    color: var(--green); -webkit-text-stroke: 2px var(--ink); paint-order: stroke fill;
  }
  .town-list {
    position: absolute; left: 30px; top: 216px; list-style: none;
    font-family: "Oswald", sans-serif; font-weight: 700; font-size: 21px; line-height: 32.4px;
    color: var(--ink); -webkit-text-stroke: 0.6px var(--yellow);
  }
  .coverage-map {
    position: absolute; left: 215px; top: 255px; width: 346px; height: 344px;
    background: linear-gradient(90deg, #e4ecd8 0%, #d6ebc4 60%, #b9e6e4 82%, #a9dcf2 100%);
  }
</style>
</head>
<body>
<div class="flyer">
  <div class="frame"></div>

  <h1 class="brand-name"><span>Fernvale</span><span>Junk Clearing</span></h1>

  <div class="service-tiles">
    <div class="tile" role="img" aria-label="Illustration of a tipper truck"></div>
    <div class="tile" role="img" aria-label="Illustration of a safety respirator mask"></div>
    <div class="tile" role="img" aria-label="Illustration of an excavator"></div>
  </div>

  <p class="tagline">local company servicing the locals<small>call today for a free quote!</small></p>

  <h2 class="services-headline">ASBESTOS REMOVAL - DEMOLITION! - RUBBISH REMOVAL!</h2>

  <p class="contact-web">
    Visit our website: <strong>www.fernvalejunkclearing.com</strong><br>
    email us: <strong>hello@fernvalejunkclearing.com</strong>
  </p>

  <section class="service-panel">
    <p class="panel-intro">For 24/7 service in the listed ereas contact us on:</p>
    <p class="supervisor">Owen Marsh - site supervisor - 0491570156</p>
    <p class="phone-feature">0491570156</p>
    <ul class="town-list">
      <li>Kempsey</li>
      <li>Taree</li>
      <li>South West Rocks</li>
      <li>foster / Tuncurry</li>
      <li>Coffs harbour</li>
      <li>Nambucca Heads</li>
      <li>Newcastle</li>
      <li>Maitland</li>
      <li>Singleton</li>
      <li>Muswellbrook</li>
      <li>Upper Hunter Valley</li>
      <li>Central Coast</li>
      <li>Tamworth</li>
    </ul>
    <div class="coverage-map" role="img" aria-label="Location map of the NSW mid north coast and Hunter region with the service area circled"></div>
  </section>
</div>
</body>
</html>
```